Business card design for IT consulting company

Looking for a simple, modern, clean business card design.
Open to reworking our existing logo.

Attached is our current business cards which we do not like.
Ideally double sided with something simple on the back.
Rectangle / Horizonal only.
No rounded edges on the card.
White as the dominate color is preferred.

Target Market(s)

clients, legal, oil & gas, medical, professionals

Industry/Entity Type

IT, tech, consulting

Contact Information for Business Card

Name, Title, email, phone, cell, website

Font styles to use
Sans Serif

Requirements
Must have
• Clean design
Should not have
• loud colors or unusual fonts, etc

```html
<!DOCTYPE html>
<html lang="en">
<head>
<meta charset="UTF-8">
<title>Nexlo Solutions – Business Card</title>
<link rel="stylesheet" href="https://fonts.googleapis.com/css2?family=Inter:wght@700&family=Mulish:wght@400;800&display=swap">
<style>
  :root {
    --backdrop: #8f8f8f;
    --card-dark: #121212;
    --card-light: #ffffff;
    --accent: #27266f;
    --accent-light: #4ab0e2;
    --text-grey: #4a4a4a;
  }
  * { margin: 0; padding: 0; box-sizing: border-box; }
  html, body { width: 1200px; height: 588px; overflow: hidden; }
  body { background: var(--backdrop); position: relative; font-family: "Mulish", sans-serif; }

  .card { position: absolute; width: 487px; height: 287px; top: 142px; }

  .card-back { left: 87px; background: var(--card-dark); display: flex; align-items: center; justify-content: center; gap: 16px; }
  .card-back .brand-square { width: 70px; height: 70px; background: var(--accent-light); flex: none; }
  .card-back .brand-name { font-family: "Inter", sans-serif; font-weight: 700; font-size: 42px; color: #ffffff; letter-spacing: -0.5px; white-space: nowrap; }

  .card-front { left: 622px; background: var(--card-light); }
  .card-front .brand { position: absolute; left: 90px; top: 88px; width: 110px; display: flex; flex-direction: column; align-items: center; gap: 10px; }
  .card-front .brand-square { width: 72px; height: 72px; background: var(--accent); }
  .card-front .brand-name { font-weight: 800; font-size: 20px; color: var(--accent); }

  .divider { position: absolute; left: 242px; top: 84px; width: 2px; height: 119px; background: var(--accent); }

  .contact { position: absolute; left: 275px; top: 80px; }
  .person-name { font-weight: 800; font-size: 19px; color: var(--accent); line-height: 1.1; }
  .person-title { font-size: 13px; color: var(--text-grey); margin-top: 2px; }
  .details { list-style: none; margin-top: 12px; }
  .details li { display: flex; align-items: center; gap: 7px; font-size: 13px; color: var(--text-grey); height: 18.5px; white-space: nowrap; }
  .details svg { width: 10px; height: 10px; flex: none; }

  .base-band { position: absolute; left: 0; bottom: 0; width: 100%; height: 12px; background: var(--accent); }
</style>
</head>
<body>
  <section class="card card-back">
    <div class="brand-square"></div>
    <div class="brand-name">Nexlo Solutions</div>
  </section>

  <section class="card card-front">
    <div class="brand">
      <div class="brand-square"></div>
      <div class="brand-name">Nexlo</div>
    </div>
    <div class="divider"></div>
    <div class="contact">
      <div class="person-name">DANIEL HART</div>
      <div class="person-title">IT Consultant</div>
      <ul class="details">
        <li><svg viewBox="0 0 10 10"><path d="M2 0.5 L3.6 2.6 L2.7 3.6 Q3.8 5.9 6.3 7.2 L7.4 6.3 L9.5 7.9 L8.4 9.5 Q4 9 0.6 2 Z" fill="var(--accent)"/></svg>(800) 555-0142</li>
        <li><svg viewBox="0 0 10 10"><rect x="2.5" y="0.5" width="5" height="9" rx="1" fill="none" stroke="var(--accent)" stroke-width="1.2"/><circle cx="5" cy="7.8" r="0.6" fill="var(--accent)"/></svg>(604) 555-0187</li>
        <li><svg viewBox="0 0 10 10"><rect x="0.5" y="2" width="9" height="6.5" fill="var(--accent)"/><path d="M0.5 2 L5 5.6 L9.5 2" fill="none" stroke="#fff" stroke-width="0.9"/></svg>daniel.hart@nexlo.ca</li>
        <li><svg viewBox="0 0 10 10"><circle cx="5" cy="5" r="4.5" fill="var(--accent)"/><path d="M3 2.5 Q5 3.5 4 5.5 Q6 6 6.5 8.5" fill="none" stroke="#fff" stroke-width="0.8"/></svg>www.nexlo.ca</li>
      </ul>
    </div>
    <div class="base-band"></div>
  </section>
</body>
</html>
```